Business card and stationnary for a doctor specialized in Orthopedic Surgery
Dr. Lucien R. Desrosiers
Business card and stationnary for a doctor specialized in Orthopedic Surgery - Medical
Creative Brief
Professional
Chirurgie Orthopédique
DO NOT LIST ADDRESS!
lucien@drdesrosiers-ortho.example
www.drdesrosiers-ortho.example
Concerning the business card, which matters most, please take into consideration the following: 1/ I need my name to be followed below it by my specialty and credentials, each on a separate line as follows Dr. Lucien R. Desrosiers Chirurgie Orthopédique Diplômé de l'UBK et l'Univ de Morvanne Ancien Interne des Hôpitaux de Clervaux 2/ I do not want any address to be listed 3/ my logo can be used either in the front but in a disrete way, or on the back as a watermark or in a corner....i will see which design is more clean and professional. 4/ Concerning the back of the business card, i need please TWO variations: - one without any text on the back except perhaps the logo or website, as u wish -and another one where you provide a place i can input four addresses myself later on ( you can write for now Hospital 1, address, tel...Hospital 2, address, tel , etc.. and i will edit them myself later on)

```html
<!DOCTYPE html>
<html lang="fr">
<head>
<meta charset="utf-8">
<title>Dr. Lucien R. Desrosiers – Cartes de visite</title>
<link href="https://fonts.googleapis.com/css2?family=Montserrat:wght@600;700&family=Open+Sans:wght@400;600&display=swap" rel="stylesheet">
<style>
  :root{
    --blue-deep:#0b3fa8;
    --blue:#1560d4;
    --blue-light:#3d8bf0;
    --grey:#b9bec6;
    --ink:#3a4250;
    --white:#ffffff;
    --stage:#eef0f3;
  }
  *{margin:0;padding:0;box-sizing:border-box}
  html,body{width:1200px;height:739px;overflow:hidden;background:var(--stage)}
  .canvas{position:relative;width:1200px;height:739px}
  .card{position:absolute;top:224px;width:500px;height:290px;border-radius:4px;overflow:hidden;box-shadow:0 10px 28px rgba(0,0,0,.18)}
  /* back */
  .card-back{left:70px;background:radial-gradient(ellipse at 45% 40%,var(--blue-light) 0%,var(--blue) 45%,var(--blue-deep) 100%)}
  .back-mark{position:absolute;left:0;right:0;top:98px;text-align:center;font-family:"Montserrat",sans-serif;font-weight:700;font-size:62px;letter-spacing:2px;color:var(--white)}
  .back-web{position:absolute;left:0;right:0;top:190px;text-align:center;font-family:"Open Sans",sans-serif;font-size:11px;letter-spacing:1.5px;color:var(--white)}
  /* front */
  .card-front{left:630px;background:var(--white)}
  .front-shape{position:absolute;inset:0}
  .front-mark{position:absolute;left:34px;top:120px;font-family:"Montserrat",sans-serif;font-weight:700;font-size:54px;letter-spacing:2px;color:var(--blue)}
  .identity{position:absolute;left:190px;top:30px;font-family:"Open Sans",sans-serif;color:var(--ink)}
  .identity .name{font-family:"Montserrat",sans-serif;font-weight:700;font-size:15px;color:var(--blue);margin-bottom:5px}
  .identity p{font-size:9.5px;line-height:1.45}
  .contacts{position:absolute;right:24px;bottom:26px;list-style:none;font-family:"Open Sans",sans-serif;font-size:9px;color:var(--white);text-align:right}
  .contacts li{display:flex;align-items:center;justify-content:flex-end;gap:6px;line-height:1.75}
  .contacts svg{width:10px;height:10px;flex:none}
</style>
</head>
<body>
<main class="canvas">
  <section class="card card-back" aria-label="Verso de la carte">
    <div class="back-mark">LRD</div>
    <div class="back-web">www.drdesrosiers-ortho.example</div>
  </section>

  <section class="card card-front" aria-label="Recto de la carte">
    <svg class="front-shape" viewBox="0 0 500 290" preserveAspectRatio="none" aria-hidden="true">
      <defs>
        <linearGradient id="frontBlue" x1="0" y1="1" x2="1" y2="0">
          <stop offset="0" stop-color="#0b3fa8"/>
          <stop offset="0.6" stop-color="#1560d4"/>
          <stop offset="1" stop-color="#3d8bf0"/>
        </linearGradient>
      </defs>
      <path d="M0 250 C160 250 330 200 420 110 C455 75 480 35 500 0 L500 290 L0 290 Z" fill="url(#frontBlue)"/>
      <path d="M0 238 C160 240 320 190 410 104 C446 70 472 32 490 0" fill="none" stroke="var(--grey)" stroke-width="7"/>
    </svg>
    <div class="front-mark">LRD</div>
    <div class="identity">
      <h1 class="name">Dr. Lucien R. Desrosiers</h1>
      <p>Chirurgie Orthopédique</p>
      <p>Diplômé de l'UBK et l'Univ de Morvanne</p>
      <p>Ancien Interne des Hôpitaux de Clervaux</p>
    </div>
    <ul class="contacts">
      <li>(555) 0 214 118
        <svg viewBox="0 0 10 10"><path d="M2 1 L4 3 L3 4 Q4 6 6 7 L7 6 L9 8 L8 9 Q3 9 1 2 Z" fill="var(--white)"/></svg></li>
      <li>lucien@drdesrosiers-ortho.example
        <svg viewBox="0 0 10 10"><rect x="1" y="2.5" width="8" height="5.5" fill="none" stroke="var(--white)"/><path d="M1 2.5 L5 6 L9 2.5" fill="none" stroke="var(--white)"/></svg></li>
      <li>bonejoint
        <svg viewBox="0 0 10 10"><circle cx="5" cy="5" r="4" fill="var(--white)"/></svg></li>
      <li>www.drdesrosiers-ortho.example
        <svg viewBox="0 0 10 10"><circle cx="5" cy="5" r="4" fill="none" stroke="var(--white)"/><path d="M1 5 H9 M5 1 Q2.5 5 5 9 M5 1 Q7.5 5 5 9" fill="none" stroke="var(--white)" stroke-width=".8"/></svg></li>
    </ul>
  </section>
</main>
</body>
</html>
```